Professional website for psychological services

Create a professional, easy to navigate website using soothing coastal images and incorporate company logo in design. Website is for a small private clinic that provides psychological services and must be appealing to professional men and women. A website I really like is www.velmorlodge.example I would love something like similar.

Target Market(s)

Professional men and women seeking psychological services

Industry/Entity Type

Mental Health

Number of Pages Required

5+ page

Requirements
Must have
• The website must incorporate the logo provided. The name of the company/website is Brindle Oak Wellness Aftercare. Colors must compliment the logo, must be coastal and soothing yet very professional. I would like a website like www.velmorlodge.example
• Pages will be:Home, Services, FAQ and Contact Us. The images included of the building and office are for the contact us page. Under the tab Servies: Individual Psychotherapy, Family Therapy, EMDR I will provide specific content for each.
Nice to have
• I want the website to be easy to navigate and the font easy to read. The writing on the logo is very light and I'm open to changing it slightly if it will be better aesthetically.
Should not have
• Please no pictures of any swimsuits, alcoholic beverages, etc. This is a professional psychological clinic.

```html
<!DOCTYPE html>
<html lang="en">
<head>
<meta charset="utf-8">
<title>Brindle Oak Wellness Aftercare</title>
<link rel="stylesheet" href="https://fonts.googleapis.com/css2?family=Cormorant+Garamond:ital,wght@0,500;0,600;1,500;1,600&family=Montserrat:wght@400;500&display=swap">
<style>
:root{
  --ink:#111213;
  --teal:#1fbcd8;
  --teal-deep:#17a9c4;
  --sand:#e3cdb2;
  --sand-line:#e6d2b8;
  --text:#5b5e62;
  --white:#ffffff;
  --serif:"Cormorant Garamond", Georgia, serif;
  --sans:"Montserrat", Arial, sans-serif;
}
*{box-sizing:border-box;margin:0;padding:0}
html,body{width:1200px;height:3191px;overflow:hidden;background:var(--white)}
body{position:relative;font-family:var(--sans);color:var(--text)}
.abs{position:absolute}

/* Header */
.site-header{left:0;top:0;width:1200px;height:94px;background:var(--ink)}
.brand{left:78px;top:22px;display:flex;align-items:center;gap:12px}
.brand-dot{width:30px;height:30px;border-radius:50%;background:var(--teal)}
.brand-name{font-family:var(--serif);font-weight:600;font-size:30px;color:var(--teal);line-height:50px}
.main-nav{right:78px;top:0;height:94px;display:flex;align-items:center;gap:38px}
.main-nav a{font-size:14px;color:var(--white);text-decoration:none;letter-spacing:.3px}
.main-nav a.current{color:var(--teal)}

/* Hero */
.hero{left:0;top:94px;width:1200px;height:640px;
  background:linear-gradient(180deg,#b9c6d6 0%,#9eafc4 22%,#6f7f96 40%,#8f9bad 55%,#dfe4ea 78%,#ffffff 100%)}
.hero-frame{left:460px;top:228px;width:278px;height:250px;border:10px solid rgba(255,255,255,.28)}
.hero-title{left:0;top:280px;width:1200px;text-align:center;font-family:var(--serif);font-style:italic;font-weight:600;font-size:100px;line-height:100px;color:var(--white)}
.hero-sub{left:0;top:400px;width:1200px;text-align:center;font-size:33px;letter-spacing:1px;color:var(--white)}

/* Welcome */
.welcome-title{left:79px;top:822px;font-family:var(--serif);font-style:italic;font-weight:600;font-size:44px;line-height:56px;color:var(--sand)}
.welcome-title span{color:var(--teal)}
.welcome-text{left:79px;top:890px;width:505px}
.welcome-text p{font-size:12.5px;line-height:25px;color:var(--text)}
.welcome-text p + p{margin-top:15px}
.btn{display:flex;align-items:center;justify-content:center;gap:18px;height:53px;border:2px solid var(--sand-line);
  font-family:var(--serif);font-weight:500;font-size:20px;letter-spacing:.5px;color:var(--teal)}
.frame-blue{left:785px;top:770px;width:336px;height:285px;border:5px solid var(--teal)}
.frame-sand{left:672px;top:949px;width:332px;height:283px;background:var(--sand)}
.portrait{left:689px;top:787px;width:417px;height:428px;
  background:linear-gradient(160deg,#6f9b52 0%,#3f6b30 40%,#5a4436 70%,#2c2f38 100%)}

/* Services */
.services{left:0;top:1324px;width:1200px;height:532px;background:var(--teal)}
.section-title{left:0;width:1200px;text-align:center;font-family:var(--serif);font-style:italic;font-weight:600;font-size:42px}
.service-card{top:1441px;width:281px;height:332px;text-align:center;color:var(--white)}
.service-card h3{position:absolute;left:0;top:168px;width:100%;font-family:var(--serif);font-weight:600;font-size:24px}
.service-card p{position:absolute;left:16px;top:209px;width:249px;font-size:11.5px;line-height:25px}
.service-icon{position:absolute;left:90px;top:45px}

/* FAQ */
.faq{left:0;top:1856px;width:1200px;height:585px;
  background:linear-gradient(180deg,#1f3140 0%,#20506a 35%,#1b6c82 60%,#13505f 100%)}
.faq-q{left:315px;width:570px;height:47px;display:flex;align-items:center;justify-content:space-between;padding:0 24px;
  background:rgba(160,170,178,.42);font-size:17px;color:var(--white)}
.faq-q.open{background:rgba(200,206,212,.35)}
.faq-a{left:337px;top:2040px;width:530px;font-size:12.5px;line-height:23px;color:var(--white)}

/* Contact */
.contact{left:0;top:2441px;width:1200px;height:562px;background:#f2f4f4}
.contact-art{left:430px;top:2441px;width:770px;height:562px;
  background:radial-gradient(ellipse at 40% 25%,#2a9fb4 0%,#7ccbd4 22%,transparent 45%),
             linear-gradient(135deg,#f2f4f4 0%,#e9e6e4 40%,#e8d9d6 60%,#b9bdb6 80%,#f2f4f4 100%)}
.field{left:79px;width:413px;border:1px solid #d6d9dc;background:rgba(255,255,255,.7);font-size:13px;color:#6a6d71;padding:12px 12px}

/* Footer */
.site-footer{left:0;top:3003px;width:1200px;height:188px;background:var(--ink)}
.footer-brand{left:0;top:3043px;width:1200px;display:flex;justify-content:center;align-items:center;gap:12px}
.copyright{left:0;top:3136px;width:1200px;text-align:center;font-size:13px;color:var(--white)}
</style>
</head>
<body>

<header class="site-header abs">
  <div class="brand abs"><span class="brand-dot"></span><span class="brand-name">Brindle Oak</span></div>
  <nav class="main-nav abs">
    <a class="current" href="#">HOME</a><a href="#">SERVICES</a><a href="#">FAQ</a><a href="#">CONTACT</a>
  </nav>
</header>

<section class="hero abs" role="img" aria-label="Snow-capped mountain peak rising above clouds"></section>
<div class="hero-frame abs"></div>
<h1 class="hero-title abs">Brindle Oak</h1>
<p class="hero-sub abs">WELLNESS AFTERCARE</p>

<h2 class="welcome-title abs">Welcome to <span>Brindle Oak</span></h2>
<div class="welcome-text abs">
  <p>Lorem Ipsum is simply dummy text of the printing and typesetting industry. Lorem Ipsum has been the industry's standard dummy text ever since the 1500s, when an unknown printer took a galley of type and scrambled it to make a type specimen book. It has survived not only five centuries, but also the leap into electronic typesetting, remaining essentially unchanged.</p>
  <p>Lorem Ipsum is simply dummy text of the printing and typesetting industry. Lorem Ipsum has been the industry's standard dummy text ever since the 1500s, when an unknown printer took a galley of type and scrambled.</p>
</div>
<div class="btn abs" style="left:77px;top:1134px;width:208px">READ MORE
  <svg width="24" height="16" viewBox="0 0 24 16"><path d="M1 8h20M14 1l7 7-7 7" fill="none" stroke="#1fbcd8" stroke-width="2"/></svg></div>
<div class="btn abs" style="left:306px;top:1134px;width:209px">CONTACT ME
  <svg width="24" height="16" viewBox="0 0 24 16"><path d="M1 8h20M14 1l7 7-7 7" fill="none" stroke="#1fbcd8" stroke-width="2"/></svg></div>
<div class="frame-sand abs"></div>
<div class="frame-blue abs"></div>
<div class="portrait abs" role="img" aria-label="Portrait of the clinic's therapist outdoors"></div>

<section class="services abs"></section>
<h2 class="section-title abs" style="top:1372px;color:var(--sand)">Services We Provide</h2>
<div class="abs" style="left:179px;top:1441px;width:842px;height:332px;background:rgba(255,255,255,.12)"></div>
<div class="abs" style="left:460px;top:1441px;width:281px;height:332px;background:rgba(255,255,255,.06)"></div>

<article class="service-card abs" style="left:179px">
  <svg class="service-icon" width="100" height="100" viewBox="0 0 100 100"><circle cx="50" cy="50" r="46" fill="none" stroke="#e3cdb2" stroke-width="4"/>
    <g fill="#fff"><circle cx="50" cy="50" r="5"/><ellipse cx="50" cy="36" rx="6" ry="9"/><ellipse cx="50" cy="64" rx="6" ry="9"/><ellipse cx="36" cy="50" rx="9" ry="6"/><ellipse cx="64" cy="50" rx="9" ry="6"/></g></svg>
  <h3>Individual Psychotherapy</h3>
  <p>Lorem Ipsum is simply dummy text of the printing and typesetting industry Lorem Ipsum has been the industry</p>
</article>
<article class="service-card abs" style="left:460px">
  <svg class="service-icon" width="100" height="100" viewBox="0 0 100 100"><circle cx="50" cy="50" r="46" fill="none" stroke="#e3cdb2" stroke-width="4"/>
    <g fill="#fff"><circle cx="39" cy="31" r="5"/><rect x="34" y="38" width="10" height="30" rx="2"/><circle cx="61" cy="31" r="5"/><path d="M61 38l9 20h-18z"/><rect x="56" y="56" width="3" height="12"/><rect x="63" y="56" width="3" height="12"/></g></svg>
  <h3>Family Therapy</h3>
  <p>Lorem Ipsum is simply dummy text of the printing and typesetting industry Lorem Ipsum has been the industry</p>
</article>
<article class="service-card abs" style="left:741px">
  <svg class="service-icon" width="100" height="100" viewBox="0 0 100 100"><circle cx="50" cy="50" r="46" fill="none" stroke="#e3cdb2" stroke-width="4"/>
    <path d="M28 50q22-24 44 0q-22 24-44 0z" fill="#fff"/><circle cx="50" cy="50" r="8" fill="#1fbcd8"/><circle cx="50" cy="50" r="3" fill="#fff"/></svg>
  <h3>EMDR</h3>
  <p>Lorem Ipsum is simply dummy text of the printing and typesetting industry Lorem Ipsum has been the industry</p>
</article>

<section class="faq abs" role="img" aria-label="Aerial view of a tropical coastline with turquoise water"></section>
<h2 class="section-title abs" style="top:1904px;color:var(--sand)">FAQ</h2>
<div class="faq-q open abs" style="top:1975px">Lorem Ipsum is simply dummy text?
  <svg width="22" height="12" viewBox="0 0 22 12"><path d="M1 11l10-10 10 10" fill="none" stroke="#fff" stroke-width="2"/></svg></div>
<p class="faq-a abs">Lorem Ipsum is simply dummy text of the printing and typesetting industry. Lorem Ipsum has been the industry's standard dummy text ever since the 1500s, when an unknown printer took a galley of type.</p>
<div class="faq-q abs" style="top:2139px">Lorem Ipsum is simply dummy text of the printing?
  <svg width="22" height="12" viewBox="0 0 22 12"><path d="M1 1l10 10 10-10" fill="none" stroke="#fff" stroke-width="2"/></svg></div>
<div class="faq-q abs" style="top:2196px">Lorem Ipsum is simply dummy text of the printing?
  <svg width="22" height="12" viewBox="0 0 22 12"><path d="M1 1l10 10 10-10" fill="none" stroke="#fff" stroke-width="2"/></svg></div>
<div class="faq-q abs" style="top:2251px">Lorem Ipsum is simply dummy text?
  <svg width="22" height="12" viewBox="0 0 22 12"><path d="M1 1l10 10 10-10" fill="none" stroke="#fff" stroke-width="2"/></svg></div>
<div class="faq-q abs" style="top:2309px">Lorem Ipsum is simply dummy text of the printing?
  <svg width="22" height="12" viewBox="0 0 22 12"><path d="M1 1l10 10 10-10" fill="none" stroke="#fff" stroke-width="2"/></svg></div>

<section class="contact abs"></section>
<div class="contact-art abs" role="img" aria-label="Aerial view of a sandy beach with turquoise surf and a coastal road"></div>
<h2 class="section-title abs" style="left:79px;top:2498px;width:auto;text-align:left;color:var(--teal)">Contact Info</h2>
<div class="field abs" style="top:2577px;height:45px">Name</div>
<div class="field abs" style="top:2634px;height:45px">Email</div>
<div class="field abs" style="top:2692px;height:45px">Phone</div>
<div class="field abs" style="top:2747px;height:105px">Messages</div>
<div class="btn abs" style="left:77px;top:2866px;width:208px">READ MORE
  <svg width="24" height="16" viewBox="0 0 24 16"><path d="M1 8h20M14 1l7 7-7 7" fill="none" stroke="#1fbcd8" stroke-width="2"/></svg></div>

<footer class="site-footer abs"></footer>
<div class="footer-brand abs"><span class="brand-dot"></span><span class="brand-name">Brindle Oak</span></div>
<p class="copyright abs">2018 ©Brindle Oak Wellness Aftercare- All Rights Reserved.</p>

</body>
</html>
```